Therapy Dog Organization Website

Looking for a website that is user friendly, welcoming, dog themed and has the following pages and links:
*Click here to join - links to a jot form
*Click here to donate - links to our paypal page
*Request a visit - links to a jot form
*Kinnect Follow Link
*Snapfolio Follow Link
*Our team - images uploaded to showcase our dogs
*Donors and Referrals Page - Where I can update as donations and referrals come in.
*Online store. Currently this is in Jot Form but I would like a store front. I would not want this to be a link but rather a hidden page, something like www.hollowbirch.org/teamstore.

Please visit www.hollowbirch.org to see what we have right now designed simply in Canva. Dog photos can be provided to use in images.

Note: I have funds from a grant that I have to spend to add gratuity to the project winner.

```html
<!DOCTYPE html>
<html lang="en">
<head>
<meta charset="utf-8">
<title>Hollow Birch — Therapy Dogs</title>
<link href="https://fonts.googleapis.com/css2?family=Fraunces:opsz,wght@9..144,600;9..144,700;9..144,800&family=Nunito:wght@400;600;700&display=swap" rel="stylesheet">
<style>
:root{
  --orange:#ff9a05;
  --gold:#f5b301;
  --ink:#1c1714;
  --body:#4a4440;
  --muted:#77706a;
  --cream:#fdf9ef;
  --card-warm:#fffbea;
  --card-warm-line:#fbe9a8;
  --card-grey:#f7f6f3;
  --card-grey-line:#ebe8e2;
  --footer:#1f1a18;
  --white:#ffffff;
  --social-a:#1877f2;
}
*{box-sizing:border-box;margin:0;padding:0}
html,body{width:1200px;height:2818px;overflow:hidden}
body{font-family:'Nunito',sans-serif;color:var(--ink);background:var(--white);position:relative}
.abs{position:absolute}
.btn{position:absolute;display:flex;align-items:center;justify-content:center;border-radius:999px;font-weight:700;font-size:13px;white-space:nowrap}
.btn-orange{background:var(--orange);color:var(--white)}
.eyebrow{font-size:11.5px;font-weight:700;letter-spacing:1.6px;color:var(--orange);text-transform:uppercase}

/* nav */
.nav{position:absolute;top:0;left:0;width:1200px;height:50px;background:var(--white);border-bottom:1px solid #eee}
.brand{position:absolute;top:13px;left:170px;display:flex;align-items:center;gap:8px;font-family:'Fraunces',serif;font-weight:700;font-size:19px;color:var(--ink)}
.brand-dot{width:14px;height:14px;border-radius:50%;background:var(--orange)}
.nav-links{position:absolute;top:17px;left:509px;display:flex;gap:22px;font-size:11.5px;color:#3b3531}
.nav-links .active{color:var(--orange);border-bottom:1.5px solid var(--orange);padding-bottom:3px}
.nav-circle{position:absolute;top:16px;width:18px;height:18px;border-radius:50%;border:2px solid #8a8580}
.nav .btn{top:10px;height:30px;font-size:11px}

/* hero */
.hero{position:absolute;top:50px;left:0;width:1200px;height:638px;background:linear-gradient(100deg,#3a3736 0%,#5b5552 30%,#7a6a5c 55%,#8d8a8c 80%,#a7a3a6 100%)}
.hero-shade{position:absolute;inset:0;background:linear-gradient(90deg,rgba(20,18,17,.45),rgba(20,18,17,.1) 70%)}
.hero-eyebrow{position:absolute;top:115px;left:361px;display:flex;align-items:center;gap:10px;color:var(--gold);font-size:11.5px;font-weight:700;letter-spacing:1.4px}
.hero-eyebrow i{width:11px;height:11px;border-radius:50%;background:var(--gold)}
.hero h1{position:absolute;top:152px;left:358px;font-family:'Fraunces',serif;font-weight:700;font-size:52px;line-height:69px;color:var(--white)}
.hero h1 .gold{color:var(--gold)}
.hero p{position:absolute;top:378px;left:359px;width:420px;font-size:15.5px;line-height:25px;color:#ece8e4}
.hero .btn{top:483px;height:44px;font-size:13px}
.btn-ghost{border:1px solid rgba(255,255,255,.6);color:var(--white);background:rgba(255,255,255,.08)}
.scroll{position:absolute;top:564px;left:0;width:1200px;text-align:center;font-size:9px;letter-spacing:1.5px;color:#ddd}
.scroll-line{position:absolute;top:583px;left:599px;width:1px;height:32px;background:rgba(255,255,255,.5)}

/* band */
.band{position:absolute;top:688px;left:0;width:1200px;height:59px;background:var(--orange);display:flex;align-items:center;justify-content:center;gap:26px;color:var(--white);font-size:11px;font-weight:700}
.band span{display:flex;align-items:center;gap:7px}
.band i{width:12px;height:12px;border-radius:3px;background:rgba(255,255,255,.6)}

/* mission */
.mission{position:absolute;top:747px;left:0;width:1200px;height:537px;background:var(--white)}
.center{position:absolute;left:0;width:1200px;text-align:center}
.mission h2{font-family:'Fraunces',serif;font-weight:700;font-size:34px;color:var(--ink)}
.card{position:absolute;top:186px;width:268px;height:277px;border-radius:18px;padding:26px 25px}
.card.warm{background:var(--card-warm);border:1px solid var(--card-warm-line)}
.card.grey{background:var(--card-grey);border:1px solid var(--card-grey-line)}
.card-icon{width:34px;height:34px;border-radius:8px;background:#e9c98a;margin-bottom:16px}
.card h3{font-family:'Fraunces',serif;font-weight:700;font-size:16.5px;line-height:22px;margin-bottom:12px}
.card p{font-size:12px;line-height:20px;color:var(--body)}

/* pack */
.pack{position:absolute;top:1284px;left:0;width:1200px;height:570px;background:var(--cream)}
.pack h2{position:absolute;top:185px;left:154px;font-family:'Fraunces',serif;font-weight:700;font-size:36px;line-height:38px}
.pack p{position:absolute;top:279px;left:154px;width:428px;font-size:13.5px;line-height:22.5px;color:var(--body)}
.pack .btn{top:370px;left:154px;width:152px;height:43px}
.tile{position:absolute;width:205px;height:205px;border-radius:12px}

/* cta */
.cta{position:absolute;top:1854px;left:0;width:1200px;height:416px;background:linear-gradient(90deg,#2e2a28 0%,#4b433f 35%,#5a4e44 60%,#3a3432 100%)}
.cta-shade{position:absolute;inset:0;background:rgba(20,16,14,.35)}
.cta-dot{position:absolute;top:82px;left:588px;width:24px;height:24px;border-radius:50%;background:var(--gold)}
.cta h2{top:131px;font-family:'Fraunces',serif;font-weight:700;font-size:36px;line-height:38px;color:var(--white)}
.cta p{top:223px;font-size:14px;line-height:22px;color:#eee;left:320px;width:560px}
.cta .btn{top:299px;height:42px;font-size:13px}

/* follow */
.follow{position:absolute;top:2270px;left:0;width:1200px;height:283px;background:var(--white)}
.follow h2{font-family:'Fraunces',serif;font-weight:700;font-size:29px;color:var(--ink)}
.follow .btn{top:179px;height:42px;font-size:11.5px;gap:9px;color:var(--white)}
.follow .btn i{width:16px;height:16px;border-radius:50%;border:2px solid var(--white)}
.btn-social-a{background:var(--social-a)}
.btn-social-b{background:linear-gradient(90deg,#f56a5c,#d63384 55%,#8f4fd6)}

/* footer */
.footer{position:absolute;top:2553px;left:0;width:1200px;height:265px;background:var(--footer);color:#bdb6b0}
.footer .brand{top:52px;left:175px;color:var(--white);font-size:19px}
.footer .tagline{position:absolute;top:89px;left:172px;font-size:10.5px}
.footer .soc{position:absolute;top:124px;width:16px;height:16px;border-radius:50%;border:2px solid #a9a29c}
.fcol{position:absolute;top:52px;font-size:10.5px}
.fcol h4{color:var(--white);font-size:10.5px;letter-spacing:1px;font-weight:700;margin-bottom:13px}
.fcol div{margin-bottom:8px}
.fline{position:absolute;top:179px;left:172px;width:856px;height:1px;background:#342d2a}
.fsmall{position:absolute;top:205px;font-size:8.5px;color:#5b534e}
</style>
</head>
<body>

<header class="nav">
  <div class="brand"><span class="brand-dot"></span>HollowBirch</div>
  <nav class="nav-links"><span class="active">Home</span><span>Our Team</span><span>Donors &amp; Referrals</span></nav>
  <span class="nav-circle" style="left:748px"></span>
  <span class="nav-circle" style="left:787px"></span>
  <a class="btn btn-orange" style="left:826px;width:118px">Click Here to Join</a>
  <a class="btn" style="left:966px;width:68px;background:var(--ink);color:var(--white)">Donate</a>
</header>

<section class="hero">
  <div class="abs" role="img" aria-label="Photo of a person hugging a golden retriever on a waterfront pier" style="inset:0"></div>
  <div class="hero-shade"></div>
  <div class="hero-eyebrow"><i></i>COMFORT • JOY • LOVE</div>
  <h1>Bringing Joy,<br><span class="gold">One Paw</span><br>at a Time.</h1>
  <p>Hollow Birch is a community of certified therapy dogs and their handlers, dedicated to spreading comfort, unconditional love, and healing one visit at a time.</p>
  <a class="btn btn-orange" style="left:358px;width:150px">Click Here to Join</a>
  <a class="btn btn-ghost" style="left:520px;width:171px">Click Here to Donate</a>
  <a class="btn btn-ghost" style="left:704px;width:139px">Request a Visit</a>
  <div class="scroll">SCROLL</div>
  <div class="scroll-line"></div>
</section>

<div class="band">
  <span><i></i>Certified Therapy Teams</span>
  <span><i></i>Hospital Visits</span>
  <span><i></i>School Reading Programs</span>
  <span><i></i>Senior Center Care</span>
  <span><i></i>501(c)(3) Nonprofit</span>
</div>

<section class="mission">
  <div class="center eyebrow" style="top:76px">Our Mission</div>
  <h2 class="center" style="top:96px">What Does a Hollow Birch Visit Look Like?</h2>
  <div class="card warm" style="left:173px">
    <div class="card-icon"></div>
    <h3>Hospitals &amp; Healthcare</h3>
    <p>Our certified dogs bring calm and warmth to patients, staff, and families during difficult moments. Studies show therapy dog visits reduce anxiety, lower blood pressure, and lift spirits.</p>
  </div>
  <div class="card grey" style="left:466px">
    <div class="card-icon" style="background:#b9c6d8"></div>
    <h3>Schools &amp; Reading<br>Programs</h3>
    <p>Children who struggle with reading gain confidence reading aloud to our non-judgmental pups. Our handlers work with educators to create meaningful, curriculum-aligned sessions.</p>
  </div>
  <div class="card warm" style="left:759px">
    <div class="card-icon" style="background:#f2c94c"></div>
    <h3>Senior Centers &amp; Assisted<br>Living</h3>
    <p>For residents living with loneliness or memory challenges, a dog's unconditional love is medicine. Our regular visits build relationships that bring lasting joy.</p>
  </div>
</section>

<section class="pack">
  <div class="abs eyebrow" style="top:161px;left:154px">The Pack</div>
  <h2>Meet the dogs who<br>make it happen.</h2>
  <p>Every member of our team is a certified therapy dog who has passed rigorous temperament and skills testing. Behind each pup is a dedicated handler committed to safe, joyful visits.</p>
  <a class="btn btn-orange">Meet Our Team →</a>
  <div class="tile" role="img" aria-label="Photo of a smiling golden retriever" style="top:75px;left:625px;background:linear-gradient(160deg,#3c3a38,#b07a3e)"></div>
  <div class="tile" role="img" aria-label="Photo of a golden retriever sitting on grass" style="top:75px;left:841px;background:linear-gradient(160deg,#6f7a3a,#d4a661 60%,#7fa043)"></div>
  <div class="tile" role="img" aria-label="Photo of a small curly dog walking toward the camera" style="top:291px;left:625px;background:linear-gradient(180deg,#aebfd6,#5e7490 70%,#3b4456)"></div>
  <div class="tile" role="img" aria-label="Photo of a happy golden retriever close up" style="top:291px;left:841px;background:linear-gradient(160deg,#f4f2f1,#e5b57c 60%,#f3efec)"></div>
</section>

<section class="cta">
  <div class="abs" role="img" aria-label="Photo of a laughing woman embracing a fluffy dog" style="inset:0"></div>
  <div class="cta-shade"></div>
  <div class="cta-dot"></div>
  <h2 class="center">Ready to bring a little joy to<br>your community?</h2>
  <p class="abs" style="text-align:center">Whether you want to schedule a visit, join our team, or support our mission — we would love to hear from you.</p>
  <a class="btn btn-orange" style="left:464px;width:137px">Request a Visit</a>
  <a class="btn" style="left:614px;width:122px;background:var(--white);color:var(--ink)">Donate Now</a>
</section>

<section class="follow">
  <div class="center eyebrow" style="top:64px">Stay Connected</div>
  <h2 class="center" style="top:84px">Follow the Pack</h2>
  <div class="center" style="top:130px;font-size:12.5px;color:var(--muted)">Get weekly updates, adorable photos, and feel-good stories straight to your feed.</div>
  <a class="btn btn-social-a" style="left:412px;width:177px"><i></i>Follow on Kinnect</a>
  <a class="btn btn-social-b" style="left:607px;width:181px"><i></i>Follow on Snapfolio</a>
</section>

<footer class="footer">
  <div class="brand"><span class="brand-dot"></span>HollowBirch</div>
  <div class="tagline">Bringing comfort, joy, and unconditional love — one paw at a time.</div>
  <span class="soc" style="left:173px"></span>
  <span class="soc" style="left:202px"></span>
  <div class="fcol" style="left:616px"><h4>NAVIGATE</h4><div>Home</div><div>Our Team</div><div>Donors &amp; Referrals</div></div>
  <div class="fcol" style="left:837px"><h4>GET INVOLVED</h4><div>Join the Pack</div><div>Request a Visit</div><div>Donate</div></div>
  <div class="fline"></div>
  <div class="fsmall" style="left:172px">© 2026 Hollow Birch · 501(c)(3) Nonprofit</div>
  <div class="fsmall" style="left:978px">Team Store</div>
</footer>

</body>
</html>
```